Bref créative |
Wordpress Website for Law Office | ||
Law Offices of Dorian Thackeray | ||
Law | ||
www.dthackerlegal.example | ||
Law Offices | ||
Clean/Simple Professional Content Driven Friendly Academic Sophisticated Elegant Service Oriented Traditional |
top | ||
www.dthackerlegal.example/logo.pdf | ||
I want my current website, dthackerlegal.example, redesigned using my logo, http://www.dthackerlegal.example/logo.pdf. The menus will be the same. The content will be the same. The layout should be similar. All I am looking for is a new design. Once the design is selected, the wordpress theme will be created based on it. |

```html
<!DOCTYPE html>
<html lang="en">
<head>
<meta charset="utf-8">
<title>Law Offices of Dorian Thackeray</title>
<link rel="stylesheet" href="https://fonts.googleapis.com/css2?family=Arimo:wght@400;700&family=Cinzel:wght@400;700&display=swap">
<style>
:root{
  --bg:#e6e8eb;
  --white:#ffffff;
  --blue:#1e5fa3;
  --blue-dark:#0f3f78;
  --blue-light:#3f86cc;
  --ink:#2b2b2b;
  --muted:#555b63;
  --grey-box:#dfe2e6;
  --grey-line:#c7ccd2;
  --dark:#3a3f45;
  --link:#1d63b5;
}
*{box-sizing:border-box;margin:0;padding:0}
html,body{width:1200px;height:991px;overflow:hidden}
body{background:var(--bg);font-family:"Arimo",Arial,sans-serif;color:var(--ink);position:relative}
a{color:var(--link)}
.page{position:absolute;left:144px;width:912px;top:0}

/* header */
.site-header{position:relative;height:130px}
.brand{position:absolute;left:6px;top:48px;display:flex;align-items:center;gap:14px}
.brand-mark{width:64px;height:64px;border-radius:50%;background:var(--blue);flex:none}
.brand-name{font-family:"Cinzel",serif;font-weight:400;color:var(--blue);line-height:1.05;white-space:nowrap}
.brand-name small{display:block;font-size:22px;color:var(--muted);text-align:center}
.brand-name strong{display:block;font-weight:400;font-size:32px}
.tollfree{position:absolute;left:170px;top:8px;background:var(--white);border:1px solid var(--grey-line);border-radius:4px;padding:6px 14px;font-size:14px;font-weight:700;color:var(--dark)}
.tollfree span{color:var(--blue)}
.scales-art{position:absolute;left:528px;top:6px;width:180px;height:122px;border-radius:6px;background:linear-gradient(180deg,#d2d6dc,#b3b9c0)}
.utility{position:absolute;right:0;top:10px;width:150px;display:flex;flex-direction:column;gap:5px}
.utility a{display:flex;align-items:center;gap:6px;background:var(--white);border:1px solid var(--grey-line);border-radius:3px;padding:4px 7px;font-size:11px;color:var(--dark);text-decoration:none}
.utility a i{width:12px;height:12px;border-radius:2px;background:var(--blue-light);display:block}
.utility a.lang{background:var(--dark);color:#fff;border-color:var(--dark)}

/* nav */
.main-nav{position:absolute;top:134px;left:0;width:912px;height:38px;background:linear-gradient(var(--blue-light),var(--blue-dark));border-radius:4px;display:flex;align-items:center;padding:0 10px}
.main-nav a{color:#fff;text-decoration:none;font-size:13px;font-weight:700;padding:0 14px;height:38px;line-height:38px;border-right:1px solid rgba(255,255,255,.2)}
.main-nav a.active{background:var(--blue-dark);box-shadow:inset 0 0 8px rgba(0,0,0,.3)}
.search{margin-left:auto;width:150px;height:22px;border-radius:11px;background:#fff;display:flex;align-items:center;justify-content:flex-end;padding-right:6px}

/* content */
.content{position:absolute;top:182px;left:0;width:912px;height:418px;background:var(--white);border:1px solid var(--grey-line);border-radius:4px;padding:18px 20px}
.welcome{position:absolute;left:22px;top:16px;width:600px;font-size:12.5px;line-height:1.45;color:var(--muted)}
.section-title{font-family:"Cinzel",serif;font-size:24px;color:var(--dark);display:flex;align-items:center;gap:10px;margin-bottom:14px}
.section-title i{width:22px;height:22px;border-radius:50%;background:var(--blue);display:block}
.welcome p{margin-bottom:11px}
.benefits{list-style:none;margin:4px 0 12px}
.benefits li{display:flex;gap:10px;align-items:flex-start;margin-bottom:8px;color:var(--ink)}
.benefits svg{flex:none;margin-top:1px}
.practice{position:absolute;right:14px;top:14px;width:252px;border:1px solid var(--grey-line);border-radius:4px;font-size:12px;line-height:1.4;color:var(--ink)}
.practice-head{background:linear-gradient(#5c636b,var(--dark));color:#fff;font-family:"Cinzel",serif;font-size:20px;padding:8px 12px;display:flex;align-items:center;gap:10px;border-radius:3px 3px 0 0}
.practice-head i{width:20px;height:20px;border-radius:50%;background:#fff;display:block}
.practice-body{padding:10px 12px}
.areas{list-style:none;margin:8px 0 10px}
.areas li{display:flex;align-items:center;gap:10px;padding:7px 0;border-bottom:1px solid #eceef1}
.areas li a{font-weight:700;text-decoration:none;font-size:13px}
.areas li i{width:18px;height:18px;border-radius:3px;background:var(--blue);display:block}
.practice-body p{margin-bottom:6px}

/* offices */
.offices{position:absolute;top:612px;left:20px;width:872px;display:grid;grid-template-columns:repeat(3,250px);justify-content:space-between;row-gap:22px}
.office{height:108px;background:linear-gradient(#eef0f2,var(--grey-box));border:1px solid var(--grey-line);border-radius:5px;text-align:center;padding-top:12px;font-size:11.5px;line-height:1.4;color:var(--ink)}
.office h3{font-family:"Cinzel",serif;font-weight:700;color:var(--blue);font-size:18px;margin-bottom:6px}

/* footer */
.site-footer{position:absolute;top:862px;left:0;width:912px;height:116px;background:linear-gradient(var(--blue-light),var(--blue));border-radius:4px;color:#fff;text-align:center}
.footer-nav{padding-top:12px;font-size:11.5px;font-weight:700}
.footer-nav a{color:#fff;text-decoration:none;margin:0 5px}
.footer-note{font-size:10.5px;line-height:1.45;width:720px;margin:8px auto 0;opacity:.92}
.footer-bottom{position:absolute;bottom:0;left:0;right:0;height:30px;border-top:1px solid rgba(255,255,255,.3);display:flex;align-items:center;justify-content:center;gap:60px;font-size:10.5px}
.social{display:flex;gap:4px}
.social i{width:13px;height:13px;border-radius:2px;background:#fff;opacity:.85;display:block}
</style>
</head>
<body>
<div class="page">
  <header class="site-header">
    <div class="brand">
      <div class="brand-mark"></div>
      <div class="brand-name"><small>Law Offices of</small><strong>Dorian Thackeray</strong></div>
    </div>
    <div class="tollfree">CALL TOLL FREE: <span>(800) 555-0199</span></div>
    <div class="scales-art" role="img" aria-label="Illustration of the scales of justice"></div>
    <nav class="utility">
      <a href="#"><i></i>Join Our Mailing List</a>
      <a href="#"><i></i>Add Site To Favorites</a>
      <a href="#"><i></i>Log Into My File 24/7</a>
      <a href="#" class="lang"><i></i>Languages Spoken</a>
    </nav>
  </header>

  <nav class="main-nav">
    <a href="#">Home Page</a>
    <a href="#" class="active">Practice Areas</a>
    <a href="#">Why Us</a>
    <a href="#">Our Fees</a>
    <a href="#">Free Advice</a>
    <a href="#">Contact Us</a>
    <a href="#">Closing Tips</a>
    <div class="search">
      <svg width="12" height="12" viewBox="0 0 12 12"><circle cx="5" cy="5" r="3.5" fill="none" stroke="#555" stroke-width="1.5"/><line x1="7.5" y1="7.5" x2="11" y2="11" stroke="#555" stroke-width="1.5"/></svg>
    </div>
  </nav>

  <main class="content">
    <section class="welcome">
      <h1 class="section-title"><i></i>Welcome to our site</h1>
      <p>The Law Offices of Dorian Thackeray is dedicated to providing the highest quality legal advice and counseling to clients throughout New York State. We offer extensive knowledge and experience in <a href="#">Real Estate</a> and <a href="#">Business Law</a>.</p>
      <p>When faced with a legal question, choosing the right law firm is a critical first step in resolving the issue. By choosing the Law Offices of Dorian Thackeray, you are choosing a firm that:</p>
      <ul class="benefits">
        <li><svg width="14" height="14" viewBox="0 0 14 14"><circle cx="7" cy="7" r="7" fill="#1e5fa3"/><path d="M5 4l4 3-4 3z" fill="#fff"/></svg>Provides individualized service that gives its clients confidence and peace of mind.</li>
        <li><svg width="14" height="14" viewBox="0 0 14 14"><circle cx="7" cy="7" r="7" fill="#1e5fa3"/><path d="M5 4l4 3-4 3z" fill="#fff"/></svg>Possesses vast experience and resources that enables it to handle your legal needs in a professional manner with efficiency, clarity, and resolve.</li>
        <li><svg width="14" height="14" viewBox="0 0 14 14"><circle cx="7" cy="7" r="7" fill="#1e5fa3"/><path d="M5 4l4 3-4 3z" fill="#fff"/></svg>Charges reasonable and straight-forward prices for the legal services rendered.</li>
      </ul>
      <p>Individuals and business entities alike have placed their trust in the Law Offices of Dorian Thackeray for one simple reason: they know they will be represented by highly skilled and dedicated attorneys who provide a level of sophistication and a value proposition that is unmatched. Please take a moment to browse through our website to learn how we can help you.</p>
    </section>

    <aside class="practice">
      <h2 class="practice-head"><i></i>Practice Areas</h2>
      <div class="practice-body">
        <p>We have extensive experience in the areas of law listed below.</p>
        <ul class="areas">
          <li><i></i><a href="#">Business Law</a></li>
          <li><i></i><a href="#">Internet Law</a></li>
          <li><i></i><a href="#">Real Estate Law</a></li>
          <li><i></i><a href="#">Wills &amp; Trusts Law</a></li>
        </ul>
        <p>Please click on the link above for a detailed description of each practice area.</p>
        <p>If you need representation in any area of law not listed above, please <a href="#">contact us</a>. We have many experienced attorneys that we work with and we will be happy to refer you to an attorney who can handle your matter.</p>
      </div>
    </aside>
  </main>

  <section class="offices">
    <div class="office"><h3>Brooklyn Office</h3>1480 E. 14th Street, 2nd Floor<br>Brooklyn, NY 11230<br>(718) 555-0142</div>
    <div class="office"><h3>Manhattan Office</h3>412 Broadway, Suite 1210<br>New York, NY 10013<br>(212) 555-0187</div>
    <div class="office"><h3>Long Island Office</h3>48 Harbor Mill Road<br>Great Neck, NY 11021<br>(516) 555-0163</div>
    <div class="office"><h3>Westchester Office</h3>215 Main Street, 4th Floor<br>White Plains, NY 10601<br>(914) 555-0128</div>
    <div class="office"><h3>Staten Island Office</h3>Coming Soon<br>Coming Soon<br>Coming Soon</div>
    <div class="office"><h3>New Jersey Office</h3>Coming Soon<br>Coming Soon<br>Coming Soon</div>
  </section>

  <footer class="site-footer">
    <nav class="footer-nav">
      <a href="#">Home</a>| <a href="#">Practice</a>| <a href="#">Areas</a>| <a href="#">Why Us</a>| <a href="#">Our Fees</a>| <a href="#">Free Advice</a>| <a href="#">Closing Tips</a>| <a href="#">Contact Us</a>| <a href="#">Languages</a>
    </nav>
    <p class="footer-note">Our attorneys provide legal services throughout the five boroughs of New York City (Brooklyn, Manhattan, Queens, Staten Island, and the Bronx), Long Island (both Nassau &amp; Suffolk), Westchester County and Upstate New York. This website constitutes attorney advertising.</p>
    <div class="footer-bottom">
      <span>© 2012 Thackeray Legal Group, All Rights Reserved.</span>
      <span>Disclaimer | Privacy Policy | Site Map</span>
      <span class="social"><i></i><i></i><i></i><i></i></span>
    </div>
  </footer>
</div>
</body>
</html>
```